4' x 8' Construction Project Sign, think of a very large business card

We need project signs for our construction sites, the sign will be mounted along the road so cars driving by can quickly read. the sign should be able to be read as cars drive by doing highway speed.

Think like your making a large business card

I would like to include "NOW HIRING" Superintendents, Project Managers, Pipe Foremen, Pipe Layers, and Equipment Operators

Description of services we provide should include

Civil Construction Services
Land Clearing
Excavation
Underground Utilities
Environmental Maintenance

The 2 objectives is to market to future clients and to recruit new employees

The sign will be mounted on posts at the entrance of our construction projects
Updates

Low design quality

Target Market(s)

Construction and land developers

Industry/Entity Type

Construction Company

Other font styles liked:
• Hypatia Sans Pro lite

Colors

Designer to choose colors to be used in the design.

Requirements
Must have
• Clean and easy to read
• Civil Construction Services
• Land Clearing
• Excavation
• Underground Utilities
• Road Construction

```html
<!DOCTYPE html>
<html lang="en">
<head>
<meta charset="utf-8">
<title>Harlow Brothers – Project Sign</title>
<link rel="stylesheet" href="https://fonts.googleapis.com/css2?family=Tenor+Sans&display=swap">
<style>
  :root {
    --brand-blue: #3b4799;
    --brand-grey: #9e9d9b;
    --paper: #ffffff;
    --frame: #c9c9c9;
  }
  html, body {
    margin: 0;
    padding: 0;
    width: 1200px;
    height: 1200px;
    overflow: hidden;
    background: var(--paper);
  }
  .sign {
    position: relative;
    width: 1200px;
    height: 1200px;
    overflow: hidden;
    font-family: "Tenor Sans", sans-serif;
  }
  .sign-frame {
    position: absolute;
    left: 65px;
    top: 65px;
    width: 1076px;
    height: 1076px;
    border: 1px solid var(--frame);
    box-sizing: border-box;
  }
  .brand-square {
    position: absolute;
    left: 142px;
    top: 109px;
    width: 162px;
    height: 162px;
    background: var(--brand-blue);
  }
  .brand-divider {
    position: absolute;
    left: 332px;
    top: 87px;
    width: 7px;
    height: 212px;
    background: var(--brand-grey);
  }
  .brand-name {
    position: absolute;
    left: 362px;
    top: 134px;
    margin: 0;
    font-size: 63px;
    line-height: 1;
    font-weight: 400;
    color: var(--brand-blue);
    white-space: nowrap;
  }
  .brand-tagline {
    position: absolute;
    left: 364px;
    top: 212px;
    margin: 0;
    font-size: 39px;
    line-height: 1;
    color: var(--brand-grey);
    white-space: nowrap;
    letter-spacing: 0.3em;
  }
  .hiring-band {
    position: absolute;
    left: 331px;
    top: 305px;
    width: 810px;
    height: 106px;
    background: var(--brand-blue);
    overflow: hidden;
  }
  .hiring-title {
    position: absolute;
    left: 35px;
    top: 24px;
    margin: 0;
    font-size: 70px;
    line-height: 1;
    font-weight: 400;
    color: var(--paper);
    white-space: nowrap;
    letter-spacing: 0.26em;
  }
  .hiring-roles {
    position: absolute;
    left: 366px;
    top: 430px;
    width: 740px;
    margin: 0;
    font-size: 55px;
    line-height: 69px;
    color: var(--brand-blue);
  }
  .services-band {
    position: absolute;
    left: 65px;
    top: 733px;
    width: 1076px;
    height: 409px;
    background: var(--brand-blue);
  }
  .services-list {
    position: absolute;
    left: 300px;
    top: 44px;
    margin: 0;
    padding: 0;
    list-style: none;
    font-size: 51px;
    line-height: 65.5px;
    color: var(--paper);
    white-space: nowrap;
  }
</style>
</head>
<body>
  <main class="sign">
    <div class="sign-frame"></div>

    <header class="brand">
      <div class="brand-square"></div>
      <div class="brand-divider"></div>
      <h1 class="brand-name">HARLOW BROTHERS</h1>
      <p class="brand-tagline">CIVIL CONSTRUCTION</p>
    </header>

    <section class="hiring">
      <div class="hiring-band">
        <h2 class="hiring-title">NOW HIRING</h2>
      </div>
      <p class="hiring-roles">Superintendents, project managers, pipe foremen, pipe layers and equipment operators</p>
    </section>

    <section class="services-band">
      <ul class="services-list">
        <li>Civil Construction Services</li>
        <li>Land Clearing</li>
        <li>Excavation</li>
        <li>Underground Utilities</li>
        <li>Environmental Maintenance</li>
      </ul>
    </section>
  </main>
</body>
</html>
```